The homepage of a website

This is a simple project that should take from you a few minutes as what is needed is the design of the homepage only, the details are in the attached zip file

Please note that KLVTA board required a special tailored design where they got some parts from the different posted designs, if you are interested please follow the instructions in the below URL and submit your new updated designs as per the instructions (P.S. I will mark the project as guaranteed as an assurance to all of you)

http://qorvinworks.example/Projects/KLVTA/Design.jpg
Updates

Please note that KLVTA board required a special tailored design where they got some parts from the different posted designs, if you are interested please follow the instructions in the below URL and submit your new updated designs as per the instructions (P.S. I will mark the project as guaranteed as an assurance to all of you) http://qorvinworks.example/Projects/KLVTA/Design.jpg

```html
<!DOCTYPE html>
<html lang="en">
<head>
<meta charset="utf-8">
<title>KLVTA – Home</title>
<link href="https://fonts.googleapis.com/css2?family=Lato:wght@400;700&display=swap" rel="stylesheet">
<style>
:root{
  --navy:#1d4b7c;
  --navy-dark:#173f69;
  --orange:#f26522;
  --orange-dark:#d94f12;
  --text:#333;
  --muted:#666;
  --grey-band:#e6e6e6;
  --line:#cfcfcf;
  --white:#fff;
}
*{box-sizing:border-box;margin:0;padding:0}
html,body{width:1200px;height:2421px;overflow:hidden}
body{font-family:'Lato',sans-serif;color:var(--text);background:var(--white);position:relative}
.btn{display:inline-block;background:var(--orange);color:#fff;font-size:13px;border-radius:3px;text-align:center}

/* top bar */
.topbar{position:absolute;top:0;left:0;width:1200px;height:47px;background:#fff}
.lang{position:absolute;left:124px;top:10px;width:70px;height:26px;line-height:26px;font-size:12px}
.search-input{position:absolute;left:201px;top:10px;width:219px;height:27px;border:1px solid #ccc;border-radius:3px;font-size:10px;color:#666;padding:7px 8px}
.search-input svg{position:absolute;right:8px;top:5px}
.login{position:absolute;left:928px;top:10px;width:62px;height:26px;line-height:26px}
.register{position:absolute;left:1006px;top:10px;width:70px;height:26px;line-height:26px}

/* header */
.header{position:absolute;top:47px;left:0;width:1200px;height:140px;border-top:1px solid #eee}
.brand{position:absolute;left:128px;top:36px;display:flex;align-items:center;gap:12px}
.brand-mark{width:56px;height:56px;border-radius:50%;background:var(--navy)}
.brand-name{font-size:30px;font-weight:700;color:var(--navy)}
.society{position:absolute;right:124px;top:28px;width:640px;text-align:right;font-size:28px;font-weight:400;color:var(--navy);line-height:1.35}

/* nav */
.nav{position:absolute;top:187px;left:0;width:1200px;height:51px;background:var(--navy)}
.nav ul{list-style:none;display:flex;position:absolute;left:122px;top:0;height:51px}
.nav li{color:#fff;font-size:14px;height:51px;line-height:51px;padding:0 20px;margin-right:12px}
.nav li.active{background:var(--orange)}

/* hero */
.hero{position:absolute;top:238px;left:0;width:1200px;height:435px;background:linear-gradient(120deg,#9cc7df 0%,#c9e2ef 35%,#7fb2d3 60%,#b9d8ea 100%)}
.hero-caption{position:absolute;left:392px;top:147px;width:408px;height:142px;background:rgba(40,70,110,.55);color:#f1f1f1;font-size:25px;font-weight:700;text-align:center;padding-top:24px;line-height:1.3}
.hero-arrow{position:absolute;top:195px;width:49px;height:49px;display:flex;align-items:center;justify-content:center}
.hero-arrow.prev{left:50px;background:var(--navy)}
.hero-arrow.next{right:49px;background:var(--orange)}

/* search + calendar */
.section-title{font-size:23px;font-weight:700;color:var(--navy)}
.member{position:absolute;top:706px;left:123px;width:383px}
.member p{font-size:12.5px;line-height:15px;margin-top:8px;text-align:justify}
.member .btn{width:116px;height:34px;line-height:34px;font-size:15px;margin-top:20px;background:linear-gradient(var(--orange),var(--orange-dark))}
.poster{position:absolute;left:531px;top:713px;width:219px;height:239px;border:1px solid #ccc;background:linear-gradient(160deg,#fff 0%,#f3e7d5 45%,#e8a46b 75%,#c9a979 100%)}
.calendar{position:absolute;left:775px;top:706px;width:302px}
.cal-head{margin-top:12px;height:38px;background:var(--navy);color:#fff;display:flex;justify-content:space-between;align-items:center;padding:0 14px;font-size:19px}
.cal{width:100%;border-collapse:collapse;font-size:13px;text-align:center}
.cal th{background:var(--orange);color:#fff;font-size:11px;height:19px;font-weight:700}
.cal td{background:#e0e0e0;height:28px;border:1px solid #fff;color:var(--navy);font-weight:700}

/* features */
.features{position:absolute;top:987px;left:0;width:1200px;height:266px;background:var(--navy)}
.card{position:absolute;top:35px;width:301px;height:196px;background:#fff;border-radius:2px;text-align:center;padding-top:18px}
.card h3{font-size:19px;font-weight:400;color:var(--navy);margin-top:10px}
.card p{font-size:12.5px;color:var(--muted);line-height:1.4;margin:6px 22px 0}

/* gallery */
.gallery{position:absolute;top:1253px;left:0;width:1200px;height:285px}
.gallery .section-title{position:absolute;left:123px;top:36px}
.thumb{position:absolute;top:90px;width:220px;height:137px;border:1px solid #9aa}
.dots{position:absolute;top:247px;left:580px;display:flex;gap:6px}
.dots span{width:8px;height:8px;border-radius:50%;background:#9aa7b8}
.dots span:first-child{background:var(--navy)}

/* news */
.news-band{position:absolute;top:1538px;left:0;width:1200px;height:362px;background:var(--grey-band)}
.col{position:absolute;top:32px;width:301px}
.item{display:flex;gap:12px;margin-top:22px;height:105px}
.item .pic{width:103px;height:103px;flex:none}
.item h4{font-size:19px;font-weight:400;color:var(--navy)}
.meta{font-size:12px;color:#777;margin:3px 0 5px}
.item p{font-size:12.5px;line-height:1.35}
.journal h4{font-size:16px;color:var(--navy);margin-top:24px}
.journal p{font-size:12.5px;line-height:1.5;margin-top:10px;text-align:justify}
.journal .btn{margin-top:20px;width:124px;height:41px;line-height:41px;font-size:15px;background:linear-gradient(var(--orange),var(--orange-dark))}

/* partners */
.partners{position:absolute;top:1900px;left:0;width:1200px;height:202px}
.partners .section-title{position:absolute;left:123px;top:30px}
.partner{position:absolute;top:78px;width:166px;height:81px;border:2px solid #d4d4d4;border-radius:3px;display:flex;align-items:center;justify-content:center}
.badge{width:60px;height:46px;border-radius:50%;background:#b7c3cf}

/* footer */
.footer{position:absolute;top:2102px;left:0;width:1200px;height:319px;background:var(--navy);color:#fff}
.fcol{position:absolute;top:38px}
.fcol h5{font-size:17px;font-weight:700;margin-bottom:18px}
.fcol ul{list-style:none;font-size:13px;line-height:21.5px}
.fcol li::before{content:"»";margin-right:12px;font-weight:700}
.fcol p{font-size:12.5px;line-height:1.5}
.email{margin-top:12px;width:220px;height:37px;background:#fff;border-radius:3px;color:#555;font-size:11px;padding:12px 10px}
.subscribe{margin-top:10px;width:94px;height:33px;line-height:33px;background:linear-gradient(var(--orange),var(--orange-dark))}
.social{display:flex;gap:10px}
.social span{width:39px;height:39px;border-radius:50%;background:#fff}
.legal{font-size:13px;line-height:21px;margin-top:16px}
</style>
</head>
<body>

<div class="topbar">
  <span class="btn lang">English ▾</span>
  <div class="search-input">Enter Any Keyword
    <svg width="16" height="16" viewBox="0 0 16 16"><circle cx="6.5" cy="6.5" r="4.5" fill="none" stroke="#f26522" stroke-width="2.2"/><line x1="10" y1="10" x2="14" y2="14" stroke="#f26522" stroke-width="2.5"/></svg>
  </div>
  <span class="btn login">Login</span>
  <span class="btn register">Register</span>
</div>

<header class="header">
  <div class="brand"><span class="brand-mark"></span><span class="brand-name">KLVTA</span></div>
  <div class="society">The Kelvata Society Of Plastic<br>&amp; Reconstructive Surgeons</div>
</header>

<nav class="nav">
  <ul>
    <li class="active">Home</li><li>Board</li><li>History</li><li>Members</li><li>Activities</li><li>Laws</li><li>Journal</li><li>Downloads</li><li>Links</li><li>Contact</li>
  </ul>
</nav>

<section class="hero" role="img" aria-label="Surgical team in blue gowns operating in a bright theatre">
  <div class="hero-arrow prev"><svg width="22" height="18" viewBox="0 0 22 18"><path d="M11 2 4 9l7 7M18 2l-7 7 7 7" fill="none" stroke="#fff" stroke-width="2.5"/></svg></div>
  <div class="hero-caption">THE KELVATA SOCIETY OF<br>PLASTIC AND RECONSTRUCTIVE<br>SERGEONS..</div>
  <div class="hero-arrow next"><svg width="22" height="18" viewBox="0 0 22 18"><path d="M4 2l7 7-7 7M11 2l7 7-7 7" fill="none" stroke="#fff" stroke-width="2.5"/></svg></div>
</section>

<section class="member">
  <h2 class="section-title">Search KLVTA Member</h2>
  <p>Nertyase riti masertas lertyars asety kertyalicabo nera faes kertyu ersvitae ertyasnemo lasec vaserat niptaiade aseoertayse. Basvolernatur aut oditaut. onseqsciunt eque porro quisquam esti doloremuia dolor.Nertyase riti masertas lertyars asety kertyalicabo nera faes kertyu ersvitae ertyasnemo lasec vaserat niptaiade aseoertayse. Basvolernatur aut oditaut. onseqsciunt eque porro quisquam esti doloremuia dolor rtyasnemo lasec vaserat niptaiade aseoertayse. Basvolernatur aut oditaut. onseqsciunt eque porro quisquam esti doloremuia dolor</p>
  <span class="btn">Search</span>
</section>

<div class="poster" role="img" aria-label="Annual meeting 2014 event poster"></div>

<section class="calendar">
  <h2 class="section-title">Event’s Calender</h2>
  <div class="cal-head"><span style="font-size:12px">◀</span><span>Jan 2015</span><span style="font-size:12px">▶</span></div>
  <table class="cal">
    <tr><th>SUN</th><th>MON</th><th>TUE</th><th>WEB</th><th>THU</th><th>FRI</th><th>SAT</th></tr>
    <tr><td>1</td><td>2</td><td>3</td><td>4</td><td>5</td><td>6</td><td>7</td></tr>
    <tr><td>8</td><td>9</td><td>10</td><td>11</td><td>12</td><td>13</td><td>14</td></tr>
    <tr><td>15</td><td>16</td><td>17</td><td>18</td><td>19</td><td>20</td><td>21</td></tr>
    <tr><td>22</td><td>23</td><td>24</td><td>25</td><td>26</td><td>27</td><td>28</td></tr>
    <tr><td>29</td><td>30</td><td>31</td><td></td><td></td><td></td><td></td></tr>
  </table>
</section>

<section class="features">
  <div class="card" style="left:123px">
    <svg width="66" height="62" viewBox="0 0 66 62" fill="#1d4b7c"><path d="M33 2 2 18h62z"/><rect x="4" y="20" width="58" height="5"/><rect x="10" y="28" width="7" height="22"/><rect x="23" y="28" width="7" height="22"/><rect x="36" y="28" width="7" height="22"/><rect x="49" y="28" width="7" height="22"/><rect x="4" y="52" width="58" height="8"/></svg>
    <h3>Universities</h3>
    <p>Asety kertyalicabo nera Nertyase riti masertas lertya asnemo lasec vaserat nipt aiadefaes kertyu ersvitae erty aseoertayse.</p>
  </div>
  <div class="card" style="left:450px">
    <svg width="66" height="62" viewBox="0 0 66 62" fill="#1d4b7c"><circle cx="20" cy="12" r="8"/><circle cx="46" cy="12" r="8"/><path d="M6 40c0-12 6-18 14-18s14 6 14 18zM32 40c0-12 6-18 14-18s14 6 14 18z"/><rect x="2" y="42" width="62" height="6"/><rect x="10" y="50" width="46" height="10"/></svg>
    <h3>E-Learning</h3>
    <p>Asety kertyalicabo nera Nertyase riti masertas lertya asnemo lasec vaserat nipt aiadefaes kertyu ersvitae erty aseoertayse.</p>
  </div>
  <div class="card" style="left:776px">
    <svg width="66" height="62" viewBox="0 0 66 62" fill="none" stroke="#1d4b7c" stroke-width="4"><path d="M12 4v18a12 12 0 0 0 24 0V4"/><path d="M24 34v10a12 12 0 0 0 24 0V32"/><circle cx="48" cy="26" r="6"/></svg>
    <h3>Patients Eduction</h3>
    <p>Asety kertyalicabo nera Nertyase riti masertas lertya asnemo lasec vaserat nipt aiadefaes kertyu ersvitae erty aseoertayse.</p>
  </div>
</section>

<section class="gallery">
  <h2 class="section-title">Gallery</h2>
  <div class="thumb" style="left:123px;background:linear-gradient(135deg,#4a6d8a,#8fb3c4)" role="img" aria-label="Surgeons operating under theatre lights"></div>
  <div class="thumb" style="left:368px;background:linear-gradient(135deg,#e8ecef,#7aa6c9)" role="img" aria-label="Doctor greeting a patient in a wheelchair"></div>
  <div class="thumb" style="left:613px;background:linear-gradient(135deg,#cfe0ea,#4d86b8)" role="img" aria-label="Doctor checking notes beside a patient in bed"></div>
  <div class="thumb" style="left:857px;background:linear-gradient(135deg,#dfe7ec,#a9c3d3)" role="img" aria-label="Smiling doctor in a white coat"></div>
  <div class="dots"><span></span><span></span><span></span></div>
</section>

<section class="news-band">
  <div class="col" style="left:123px">
    <h2 class="section-title">News</h2>
    <div class="item"><div class="pic" style="background:linear-gradient(135deg,#35536c,#8aaec4)" role="img" aria-label="Surgeons in theatre"></div><div><h4>Lorem Ipsum</h4><div class="meta">Posted By 03 Jan 2015</div><p>Praesent vestibulum aenean nonummy hendrerit mauris. Cum sociis natoque enatibus et magnis</p></div></div>
    <div class="item"><div class="pic" style="background:linear-gradient(135deg,#4b6478,#a8bfcd)" role="img" aria-label="Operating team at work"></div><div><h4>Lorem Ipsum</h4><div class="meta">Posted By 03 Jan 2015</div><p>Praesent vestibulum aenean nonummy hendrerit mauris. Cum sociis natoque enatibus et magnis</p></div></div>
  </div>
  <div class="col" style="left:450px">
    <h2 class="section-title">Upcoming Events</h2>
    <div class="item"><div class="pic" style="background:linear-gradient(135deg,#7fa9a3,#d4e4e6)" role="img" aria-label="Surgeon in green scrubs"></div><div><h4>Lorem Ipsum</h4><div class="meta">Posted By 03 Jan 2015</div><p>Praesent vestibulum aenean nonummy hendrerit mauris. Cum sociis natoque enatibus et magnis</p></div></div>
    <div class="item"><div class="pic" style="background:linear-gradient(135deg,#c9d9e6,#5f8fb7)" role="img" aria-label="Surgical team in blue gowns"></div><div><h4>Lorem Ipsum</h4><div class="meta">Posted By 03 Jan 2015</div><p>Praesent vestibulum aenean nonummy hendrerit mauris. Cum sociis natoque enatibus et magnis</p></div></div>
  </div>
  <div class="col journal" style="left:776px">
    <h2 class="section-title">KLVTA Journal</h2>
    <h4>Publishing Infomation</h4>
    <div class="meta">Posted By 03 Jan 2015</div>
    <p>Lorem ipsum dolor sit amet conse ctetur adipisicing elit, sed do eiusmod tempor incididunt ut labore et dolore magna aliqua. Ut enim ad minim veniam, quis nostrud exercitation ullamco laboris nisi ut aliquip ex ea commodo consequat. Lorem ipsum dolor sit amet conse ctetur adipisicing elit,</p>
    <span class="btn">View Details</span>
  </div>
</section>

<section class="partners">
  <h2 class="section-title">Our Partners</h2>
  <div class="partner" style="left:123px"><span class="badge"></span></div>
  <div class="partner" style="left:320px"><span class="badge" style="border-radius:4px;width:90px;height:24px"></span></div>
  <div class="partner" style="left:516px"><span class="badge"></span></div>
  <div class="partner" style="left:713px"><span class="badge" style="border-radius:4px;width:90px;height:24px"></span></div>
  <div class="partner" style="left:910px"><span class="badge" style="width:50px;height:50px"></span></div>
</section>

<footer class="footer">
  <div class="fcol" style="left:125px"><h5>Quick Links</h5><ul><li>Home</li><li>About us</li><li>Law &amp; Regulation</li><li>Gallery</li><li>News Letter</li><li>Contact</li></ul></div>
  <div class="fcol" style="left:287px"><h5>Quick Links</h5><ul><li>Home</li><li>About us</li><li>Law &amp; Regulation</li><li>Gallery</li><li>News Letter</li><li>Contact</li></ul></div>
  <div class="fcol" style="left:450px"><h5>Quick Links</h5><ul><li>Home</li><li>About us</li><li>Law &amp; Regulation</li><li>Gallery</li><li>News Letter</li><li>Contact</li></ul></div>
  <div class="fcol" style="left:613px;width:222px"><h5>News Latter Signup</h5><p>Entere Your Email And Subscribe Our Bio Monthy News Latter</p><div class="email">Enter Your Email Address</div><div class="btn subscribe">Subscribe</div></div>
  <div class="fcol" style="left:857px;width:220px"><h5>Follow Us On</h5>
    <div class="social" aria-label="Social links"><span></span><span></span><span></span><span></span></div>
    <div class="legal">Terms &amp; Conditions<br>Privacy Policy</div>
    <p style="margin-top:10px;font-size:13px">© copyrights KLVTA by klvta.example<br>2015. All right reservds.</p>
  </div>
</footer>

</body>
</html>
```